Business Card for TVK, logo files already created

Please, can you assist with creating a Business card the TVK graphics which are already listed on www.brinmoretech.example
The business card should be modern and upmarket, textured designs are welcome. Please feel free to express yourself and be very bold with your design.

Target Market(s)

Cyber Security

Industry/Entity Type

Information Technology

Contact Information for Business Card

Company Name
Name
Title
Mobile
Fax or Tel
email
url

Font styles to use
Serif
Sans Serif

Colors
3277b5
85acd3
ffffff

```html
<!DOCTYPE html>
<html lang="en">
<head>
<meta charset="utf-8">
<title>TVK Business Card</title>
<link href="https://fonts.googleapis.com/css2?family=Roboto:wght@300;400;700&display=swap" rel="stylesheet">
<style>
  :root {
    --brand-blue: #24409a;
    --paper: #ffffff;
    --stage: #2b2d31;
    --contact-text: #dfe5f5;
  }
  * { margin: 0; padding: 0; box-sizing: border-box; }
  html, body { width: 1200px; height: 900px; overflow: hidden; }
  body {
    background: var(--stage);
    font-family: "Roboto", Arial, sans-serif;
    position: relative;
  }
  .card {
    position: absolute;
    border-radius: 22px;
    overflow: hidden;
    background: var(--brand-blue);
  }
  .card-front {
    left: 560px; top: 150px;
    width: 560px; height: 320px;
  }
  .card-front .band {
    position: absolute;
    left: 0; right: 0; top: 60px; height: 150px;
    background: var(--paper);
    display: flex; align-items: center; justify-content: center;
  }
  .card-back {
    left: 90px; top: 180px;
    width: 320px; height: 560px;
  }
  .card-back .top {
    position: absolute; left: 0; right: 0; top: 0; height: 245px;
    background: var(--paper);
    display: flex; align-items: center; justify-content: center;
  }
  .brand-name {
    display: flex; align-items: center; gap: 12px;
    font-weight: 700;
    color: var(--brand-blue);
    letter-spacing: 3px;
    line-height: 1;
  }
  .brand-name .mark {
    background: var(--brand-blue);
    flex: none;
  }
  .card-front .brand-name { font-size: 44px; }
  .card-front .brand-name .mark { width: 22px; height: 22px; }
  .card-back .brand-name { font-size: 38px; }
  .card-back .brand-name .mark { width: 19px; height: 19px; }

  .person {
    position: absolute; left: 150px; top: 285px;
    color: var(--paper);
  }
  .person .name { font-size: 19px; font-weight: 700; }
  .person .title { font-size: 16px; font-weight: 300; margin-top: 2px; }
  .contacts {
    position: absolute; left: 60px; top: 375px;
    list-style: none;
  }
  .contacts li {
    display: flex; align-items: center;
    height: 26px;
    font-size: 12px; letter-spacing: 1.4px;
    color: var(--contact-text);
    white-space: nowrap;
  }
  .contacts svg { width: 13px; height: 13px; margin-right: 18px; fill: var(--contact-text); flex: none; }
</style>
</head>
<body>

  <div class="card card-front">
    <div class="band">
      <div class="brand-name"><span class="mark"></span>TVK</div>
    </div>
  </div>

  <div class="card card-back">
    <div class="top">
      <div class="brand-name"><span class="mark"></span>TVK</div>
    </div>

    <div class="person">
      <div class="name">Aria Lennox</div>
      <div class="title">Founder</div>
    </div>

    <ul class="contacts">
      <li>
        <svg viewBox="0 0 16 16" aria-hidden="true"><rect x="4" y="1" width="8" height="14" rx="1.5"/><rect x="5.5" y="3" width="5" height="8" fill="#24409a"/></svg>
        +999 999 9999
      </li>
      <li>
        <svg viewBox="0 0 16 16" aria-hidden="true"><path d="M3.5 1.5l3 3-1.6 1.8c.9 2 2.4 3.6 4.4 4.5l1.8-1.7 3 3-1.8 2C7 13.4 2.6 9 1.5 3.3z"/></svg>
        +999 999 9999
      </li>
      <li>
        <svg viewBox="0 0 16 16" aria-hidden="true"><rect x="1" y="3" width="14" height="10" rx="1"/><path d="M1.5 3.5L8 9l6.5-5.5" stroke="#24409a" stroke-width="1.3" fill="none"/></svg>
        hello@brinmoretech.example
      </li>
      <li>
        <svg viewBox="0 0 16 16" aria-hidden="true"><circle cx="8" cy="8" r="7"/><path d="M1 8h14M8 1c-3 3-3 11 0 14M8 1c3 3 3 11 0 14" stroke="#24409a" stroke-width="1" fill="none"/></svg>
        www.brinmoretech.example
      </li>
    </ul>
  </div>

</body>
</html>
```